Poster Design Project - Front Window Poster for IT Business

Design a poster to be displayed in the front window of our office.
To include the following text:
Proactive Network Solutions
Servers & Networks
Workly 480
Cloud Solutions
Helpdesk Services & Support
Network Audits
Disaster Recovery
IT Consulting
Contact details to be shown on the poster:
www.qe.com.au
02 5550 1824
Please also include the logo and related colour scheme.
Needs to look professional and easy to read from the street.
Must be in A1 format, printable through quillomark.
Hi Designers,
Nadia

```html
<!DOCTYPE html>
<html lang="en">
<head>
<meta charset="utf-8">
<title>We Offer – QE Technology Solutions</title>
<link rel="stylesheet" href="https://fonts.googleapis.com/css2?family=Arimo:wght@400;700&family=Montserrat:wght@900&family=Tinos&display=swap">
<style>
  :root {
    --band-blue: #0a3bc4;
    --title-cyan: #00eefc;
    --title-shadow: #1f4fd6;
    --rule-cyan: #5ff5f7;
    --bullet-cyan: #00e5f5;
    --ink: #0b0b0b;
    --contact-blue: #1c42c9;
    --paper: #ffffff;
  }
  html, body {
    margin: 0;
    padding: 0;
    overflow: hidden;
    background: var(--paper);
  }
  .poster {
    position: relative;
    width: 854px;
    height: 1200px;
    overflow: hidden;
    background: var(--paper);
    font-family: "Arimo", Arial, sans-serif;
  }
  .band {
    position: absolute;
    left: 0;
    width: 100%;
    height: 66px;
    background: var(--band-blue);
  }
  .band--top { top: 0; }
  .band--bottom { bottom: 0; height: 67px; }

  .headline {
    position: absolute;
    top: 62px;
    left: 0;
    width: 100%;
    margin: 0;
    text-align: center;
    white-space: nowrap;
    font-family: "Montserrat", "Arial Black", sans-serif;
    font-weight: 900;
    font-size: 165px;
    line-height: 1;
  }
  .headline-text {
    display: inline-block;
    letter-spacing: -3px;
    color: var(--title-cyan);
    text-shadow: 5px 5px 0 var(--title-shadow);
    transform: scaleX(0.8);
    transform-origin: 50% 0;
  }
  .headline-pixels {
    position: absolute;
    left: 174px;
    top: 188px;
  }
  .headline-rule {
    position: absolute;
    top: 227px;
    height: 9px;
    background: var(--rule-cyan);
  }
  .headline-rule--short { left: 58px; width: 102px; }
  .headline-rule--long { left: 237px; width: 561px; }

  .services {
    position: absolute;
    top: 280px;
    left: 128px;
    margin: 0;
    padding: 0;
    list-style: none;
  }
  .service {
    position: relative;
    height: 89.5px;
    padding-left: 35px;
    font-size: 46px;
    line-height: 60px;
    white-space: nowrap;
    color: var(--ink);
  }
  .service::before {
    content: "";
    position: absolute;
    left: 0;
    top: 22px;
    width: 18px;
    height: 18px;
    background: var(--bullet-cyan);
  }

  .contact {
    position: absolute;
    left: 122px;
    margin: 0;
    display: flex;
    align-items: center;
    gap: 16px;
    font-family: "Tinos", "Times New Roman", serif;
    font-size: 30px;
    letter-spacing: 1px;
    white-space: nowrap;
    color: var(--contact-blue);
  }
  .contact--web { top: 1020px; }
  .contact--phone { top: 1079px; }
  .contact svg { flex: none; }

  .brand {
    position: absolute;
    right: 36px;
    top: 1052px;
    display: flex;
    align-items: center;
    gap: 10px;
    white-space: nowrap;
    font-family: "Arimo", Arial, sans-serif;
    font-weight: 700;
    font-size: 22px;
    color: var(--band-blue);
  }
  .brand-square {
    width: 16px;
    height: 16px;
    background: var(--bullet-cyan);
  }
</style>
</head>
<body>
<main class="poster">
  <div class="band band--top"></div>

  <h1 class="headline"><span class="headline-text">WE OFFER</span></h1>
  <svg class="headline-pixels" width="50" height="42" viewBox="0 0 50 42" aria-hidden="true">
    <rect x="24" y="0" width="12" height="8" fill="#1f4fd6"/>
    <rect x="38" y="2" width="8" height="6" fill="#00eefc"/>
    <rect x="16" y="10" width="18" height="14" fill="#00eefc"/>
    <rect x="0" y="20" width="12" height="14" fill="#00eefc"/>
    <rect x="36" y="12" width="10" height="8" fill="#1f4fd6"/>
  </svg>
  <div class="headline-rule headline-rule--short"></div>
  <div class="headline-rule headline-rule--long"></div>

  <ul class="services">
    <li class="service">Proactive Network Solutions</li>
    <li class="service">Servers &amp; Networks</li>
    <li class="service">Workly 480</li>
    <li class="service">Cloud Solutions</li>
    <li class="service">Helpdesk Services &amp; Support</li>
    <li class="service">Network Audits</li>
    <li class="service">Disaster Recovery</li>
    <li class="service">IT Consulting</li>
  </ul>

  <p class="contact contact--web">
    <svg width="27" height="24" viewBox="0 0 27 24" aria-hidden="true">
      <path d="M13.5 0 L27 12 H23 V24 H16 V16 H11 V24 H4 V12 H0 Z" fill="#00a8f0"/>
    </svg>
    <span>www.qe.com.au</span>
  </p>
  <p class="contact contact--phone">
    <svg width="27" height="28" viewBox="0 0 27 28" aria-hidden="true">
      <rect x="0" y="0" width="27" height="6" fill="#00a8f0"/>
      <rect x="2" y="7" width="23" height="21" fill="#00a8f0"/>
      <g fill="#fff">
        <rect x="5" y="11" width="4" height="3"/><rect x="11.5" y="11" width="4" height="3"/><rect x="18" y="11" width="4" height="3"/>
        <rect x="5" y="16.5" width="4" height="3"/><rect x="11.5" y="16.5" width="4" height="3"/><rect x="18" y="16.5" width="4" height="3"/>
        <rect x="5" y="22" width="4" height="3"/><rect x="11.5" y="22" width="4" height="3"/><rect x="18" y="22" width="4" height="3"/>
      </g>
    </svg>
    <span>02 5550 1824</span>
  </p>

  <div class="brand">
    <span class="brand-square"></span>
    <span>QE Technology Solutions</span>
  </div>

  <div class="band band--bottom"></div>
</main>
</body>
</html>
```